Social Media Graphics - Harbor Climb REVISED

Create 6-7 individual social media graphics (square size) to encourage folks to join our online course called:

The Lantern Ledger Plan
How to Launch a Multi-Million Business From Scratch
Sign Up Today!

IMPORTANT: Make the largest and most prominent text on the graphic be: How to Launch a Multi-Million Business From Scratch

For the color scheme of the graphics, let's try a blue color palette; make sure the graphics appeal to both men and women

Make sure each graphic contains 1 of the 3 pics attached (crop pic as needed); and make sure one of the graphics is all TEXT only.

Target Market(s)

men and women looking to start a business

Industry/Entity Type

Entrepreneurship

Colors
0054AA
0677BA
7BADD7
CADEEF
E8F1F8

Requirements
Must have
• All the text and use the 3 pics provided; one graphic can be all text; Simple, modern design that's easy to read

```html
<!DOCTYPE html>
<html lang="en">
<head>
<meta charset="utf-8">
<title>The Lantern Ledger Plan – Social Graphics</title>
<link href="https://fonts.googleapis.com/css2?family=Montserrat:wght@600;700;800;900&display=swap" rel="stylesheet">
<style>
  :root{
    --navy:#0a1a5c;
    --navy-deep:#061241;
    --blue:#0054AA;
    --blue-mid:#0677BA;
    --blue-soft:#7BADD7;
    --blue-pale:#CADEEF;
    --blue-mist:#E8F1F8;
    --yellow:#ffc61a;
    --pink:#f7cdd6;
    --white:#ffffff;
    --page:#eef3fb;
  }
  *{margin:0;padding:0;box-sizing:border-box}
  html,body{width:1200px;height:2400px;overflow:hidden}
  body{background:var(--page);font-family:"Montserrat",Arial,sans-serif;position:relative}

  .tile{position:absolute;width:560px;height:560px;overflow:hidden}
  .tile--text{left:24px;top:20px;background:linear-gradient(160deg,#0b2a90 0%,var(--blue) 60%,#0a2f86 100%)}
  .tile--duo-top{left:616px;top:20px;background:var(--white)}
  .tile--office-right{left:24px;top:608px;background:linear-gradient(135deg,var(--navy) 0%,var(--blue) 100%)}
  .tile--framed{left:616px;top:608px;background:linear-gradient(150deg,var(--blue) 0%,#0a2f86 100%)}
  .tile--duo-left{left:24px;top:1200px;background:var(--white)}
  .tile--office-left{left:616px;top:1200px;background:linear-gradient(140deg,#0a2f86 0%,var(--blue) 100%)}
  .tile--feature{left:320px;top:1820px;background:var(--white)}

  .photo{position:absolute}
  .photo--warm{background:linear-gradient(135deg,#f2e6e4 0%,#d8b3a4 55%,#8a5a48 100%)}
  .photo--office{background:linear-gradient(160deg,#e9ecef 0%,#b9c2cc 50%,#4a4f5c 100%)}

  .label{position:absolute;font-weight:800;text-transform:uppercase;letter-spacing:.5px;white-space:nowrap}
  .label--plain{color:var(--white);font-size:15px}
  .label--navy{background:var(--navy);color:var(--white);font-size:14px;padding:10px 18px}
  .label--yellow{background:var(--yellow);color:var(--navy);font-size:14px;padding:10px 18px}
  .label--circle{width:150px;height:150px;border-radius:50%;background:var(--navy);color:var(--white);font-size:17px;line-height:1.2;white-space:normal;display:flex;align-items:center;justify-content:center;text-align:center;padding:18px}

  .headline{position:absolute;font-weight:900;text-transform:uppercase;line-height:.98;color:var(--white)}
  .headline span{display:block;white-space:nowrap}
  .hl-small{font-size:.5em;font-weight:800;letter-spacing:.5px}
  .hl-big{font-size:1em}
  .hl-accent{font-size:1.3em;color:var(--yellow)}
  .headline--center{text-align:center;left:0;right:0}
  .headline--dark{color:var(--navy)}
  .headline--dark .hl-accent{color:var(--blue)}

  .cta{position:absolute;background:var(--yellow);color:var(--navy);font-weight:800;text-transform:uppercase;white-space:nowrap;display:flex;align-items:center;justify-content:center}
  .cta--pill{border-radius:10px}
  .panel{position:absolute}
</style>
</head>
<body>

<!-- Tile 1: text only -->
<section class="tile tile--text">
  <svg width="560" height="560" style="position:absolute;left:0;top:0" aria-hidden="true">
    <g stroke="#3d6fd0" stroke-opacity=".35" stroke-width="1">
      <line x1="0" y1="140" x2="560" y2="140"/><line x1="0" y1="240" x2="560" y2="240"/>
      <line x1="0" y1="340" x2="560" y2="340"/><line x1="0" y1="440" x2="560" y2="440"/>
    </g>
    <polyline points="0,420 80,380 150,400 230,320 310,340 390,250 470,270 560,170" fill="none" stroke="#7BADD7" stroke-opacity=".5" stroke-width="3"/>
    <rect x="0" y="500" width="560" height="60" fill="#071a5a" fill-opacity=".8"/>
  </svg>
  <div class="label label--plain" style="left:0;right:0;top:26px;text-align:center">The Lantern Ledger Plan</div>
  <div class="headline headline--center" style="top:110px;font-size:64px">
    <span class="hl-small">How to Launch a</span>
    <span class="hl-big">Multi-Million</span>
    <span class="hl-accent">Business</span>
    <span class="hl-small">From Scratch</span>
  </div>
  <div class="cta cta--pill" style="left:180px;top:420px;width:200px;height:52px;font-size:17px">Sign Up Today!</div>
</section>

<!-- Tile 2 -->
<section class="tile tile--duo-top">
  <div class="panel" style="left:0;top:0;width:200px;height:300px;background:var(--pink)"></div>
  <div class="photo photo--warm" role="img" aria-label="Photo of a smiling businesswoman and businessman" style="left:40px;top:40px;width:520px;height:290px"></div>
  <div class="label label--navy" style="left:300px;top:0">The Lantern Ledger Plan</div>
  <div class="panel" style="left:470px;top:330px;width:90px;height:230px;background:var(--blue)"></div>
  <div class="headline headline--dark" style="left:36px;width:420px;text-align:center;top:346px;font-size:44px">
    <span class="hl-small">How to Launch a</span>
    <span class="hl-big">Multi-Million</span>
    <span class="hl-accent">Business</span>
    <span class="hl-small">From Scratch</span>
  </div>
  <div class="cta" style="left:0;top:516px;width:170px;height:44px;font-size:15px">Sign Up Today!</div>
</section>

<!-- Tile 3 -->
<section class="tile tile--office-right">
  <div class="photo photo--office" role="img" aria-label="Photo of a businessman and businesswoman talking in an office" style="left:220px;top:0;width:340px;height:330px"></div>
  <div class="label label--yellow" style="left:0;top:24px">The Lantern Ledger Plan</div>
  <div class="panel" style="left:0;top:280px;width:410px;height:280px;background:var(--navy)"></div>
  <div class="headline" style="left:26px;top:304px;font-size:42px">
    <span class="hl-small">How to Launch a</span>
    <span class="hl-big">Multi-Million</span>
    <span class="hl-accent">Business</span>
    <span class="hl-small">From Scratch</span>
  </div>
  <div class="cta cta--pill" style="left:420px;top:490px;width:128px;height:40px;font-size:13px">Sign Up Today!</div>
</section>

<!-- Tile 4 -->
<section class="tile tile--framed">
  <div class="photo photo--warm" role="img" aria-label="Photo of a businessman and businesswoman smiling together" style="left:130px;top:36px;width:400px;height:260px;border-radius:14px"></div>
  <div class="label label--yellow" style="left:0;top:36px">The Lantern Ledger Plan</div>
  <div class="headline headline--center" style="top:300px;font-size:52px">
    <span class="hl-small">How to Launch a</span>
    <span class="hl-big">Multi-Million</span>
    <span class="hl-accent">Business</span>
    <span class="hl-small">From Scratch</span>
  </div>
  <div class="cta cta--pill" style="left:210px;top:512px;width:140px;height:36px;font-size:13px">Sign Up Today!</div>
</section>

<!-- Tile 5 -->
<section class="tile tile--duo-left">
  <div class="panel" style="left:0;top:0;width:560px;height:200px;background:var(--pink)"></div>
  <div class="photo photo--warm" role="img" aria-label="Photo of a smiling businesswoman and businessman" style="left:0;top:40px;width:400px;height:320px"></div>
  <div class="label" style="left:400px;top:40px;color:var(--navy);font-size:26px;line-height:1.1;white-space:normal;width:150px">The Lantern Ledger Plan</div>
  <div class="panel" style="left:150px;top:270px;width:410px;height:210px;background:var(--navy)"></div>
  <div class="headline" style="left:172px;top:290px;font-size:42px">
    <span class="hl-small">How to Launch a</span>
    <span class="hl-big">Multi-Million</span>
    <span class="hl-accent">Business</span>
    <span class="hl-small">From Scratch</span>
  </div>
  <div class="cta" style="left:0;top:480px;width:560px;height:80px;font-size:24px">Sign Up Today!</div>
</section>

<!-- Tile 6 -->
<section class="tile tile--office-left">
  <svg width="560" height="560" style="position:absolute;left:0;top:0" aria-hidden="true">
    <circle cx="470" cy="190" r="170" fill="#0677BA" fill-opacity=".5"/>
  </svg>
  <div class="photo photo--office" role="img" aria-label="Photo of a businesswoman and businessman in an office" style="left:0;top:30px;width:330px;height:290px"></div>
  <div class="label label--yellow" style="right:0;top:30px">The Lantern Ledger Plan</div>
  <div class="headline headline--center" style="top:300px;font-size:52px">
    <span class="hl-small">How to Launch a</span>
    <span class="hl-big">Multi-Million</span>
    <span class="hl-accent">Business</span>
    <span class="hl-small">From Scratch</span>
  </div>
  <div class="cta cta--pill" style="left:210px;top:510px;width:140px;height:36px;font-size:13px">Sign Up Today!</div>
</section>

<!-- Tile 7 -->
<section class="tile tile--feature">
  <div class="photo photo--office" role="img" aria-label="Photo of a businesswoman and businessman talking in a bright office" style="left:0;top:0;width:560px;height:340px"></div>
  <div class="label label--circle" style="right:24px;top:24px">The Lantern Ledger Plan</div>
  <div class="panel" style="left:0;top:290px;width:560px;height:200px;background:var(--navy)"></div>
  <div class="headline headline--center" style="top:298px;font-size:50px">
    <span class="hl-small">How to Launch a</span>
    <span class="hl-big">Multi-Million</span>
    <span class="hl-accent">Business</span>
    <span class="hl-small">From Scratch</span>
  </div>
  <div class="cta" style="left:0;top:490px;width:560px;height:70px;font-size:24px">Sign Up Today!</div>
</section>

</body>
</html>
```